House Church design model for faith-based organization

A design is needed for a house church model (Christian, faith-based). I’m looking for a graphic to convey four house church hallmarks showing the balance of member engagement. The four-part model includes - God’s Presence, Community, Discipleship, Outreach. The model should consist of the text for the four parts and the words - House Church

Perhaps a circular/modular design with House Church in the center. Using equally-sized interlocking slices or winged parts (graphically speaking, but not angelic wings) may help convey a balanced approach. It isn’t a process and should not appear in progressive steps, but the order (as listed) is used when explaining the concept. The model will be used for members to evaluate monthly focus.

I’m open to interpretation of the design and artwork. Designers should not feel a need to utilize cliché-like Christian symbols. However, if done minimally (and perhaps first century-like), they could be of interest (but are not required). Keeping it abstract may help readability and convey a roots/back-to-basics feel.

The artwork will be used for a video and PowerPoint presentation. It should be vector-based for simple movement/animation.

Additional thoughts:
Readable, not complex
Interesting interlocking design found at: https://www.plorvexia.com/circle-element-infographic-options-parts-steps-template-cycle-diagram-graph-round-chart-image572914386

Target Market(s)

To existing members (for reflection) and for those seeking a simpler church experience.

Requirements
Must have
• Simple, readable design, ability to reproduce for PowerPoint, video, and web. Prefer simple illustrations rather than images.
Nice to have
• The design should create a calming sense of focus on four priorities vs. the complexity of structure/requirements often found in the church experience.
Should not have
• Not crazy about puzzle pieces. Please avoid using all CAPS and serif fonts. Should not use complex images or photos.

```html
<!DOCTYPE html>
<html lang="en">
<head>
<meta charset="utf-8">
<title>House Church Model</title>
<link href="https://fonts.googleapis.com/css2?family=Roboto:wght@400;700&display=swap" rel="stylesheet">
<style>
  :root {
    --bg: #ffffff;
    --presence: #f0b820;
    --community: #7abb25;
    --discipleship: #d23144;
    --outreach: #f25c40;
    --label: #111111;
    --title: #333333;
  }
  html, body {
    margin: 0;
    padding: 0;
    overflow: hidden;
    background: var(--bg);
  }
  .canvas {
    position: relative;
    width: 1200px;
    height: 1000px;
    overflow: hidden;
    background: var(--bg);
    font-family: "Roboto", Arial, sans-serif;
  }
  .model-artwork {
    position: absolute;
    left: 270px;
    top: 170px;
    width: 660px;
    height: 660px;
    border-radius: 50%;
    background:
      radial-gradient(circle at 50% 50%, rgba(255,255,255,0.92) 0%, rgba(255,255,255,0.55) 38%, rgba(255,255,255,0) 70%),
      conic-gradient(from -45deg,
        var(--presence) 0deg 90deg,
        var(--community) 90deg 180deg,
        var(--discipleship) 180deg 270deg,
        var(--outreach) 270deg 360deg);
    filter: blur(0.5px);
  }
  .label {
    position: absolute;
    width: 160px;
    transform: translate(-50%, -50%);
    text-align: center;
    font-size: 22px;
    line-height: 28px;
    font-weight: 400;
    color: var(--label);
  }
  .title {
    position: absolute;
    left: 601px;
    top: 500px;
    transform: translate(-50%, -50%);
    white-space: nowrap;
    font-size: 31px;
    font-weight: 700;
    color: var(--title);
  }
</style>
</head>
<body>
<div class="canvas">
  <div class="model-artwork" role="img" aria-label="Four interlocking coloured rings around a central cross, one ring for each house church hallmark"></div>

  <div class="label label-presence" style="left:600px;top:311px;">God’s<br>Presence</div>
  <div class="label label-community" style="left:782px;top:500px;">Community</div>
  <div class="label label-discipleship" style="left:604px;top:691px;">Discipleship</div>
  <div class="label label-outreach" style="left:416px;top:500px;">Outreach</div>
  <div class="title">House Church</div>
</div>
</body>
</html>
```